Business Card

I need a business card for a nutrition/fitness consultant. We are a personalized and online service that caters to developing individual plans based on persons needs. I will send you information to need on card as well as logo. Last business card was grey background and writing was black and red. I think a pic on the backside (maybe a photo that is on the app) would be good?

AskMarlene (Ill send you logo)
Marlene Tovak, Registered Nurse and Certified Sports Nutrionist (R.N., C.S.N.)
Personalized Nutrition and Fitness Architecture

1-800-555-0147 office
(305) 555-0182 cell
website www.askmarlene-example.com
marlene@askmarlene-example.com

Two locations so maybe two cards
2817 Willowmere Lane, inside Palmetto Glow Studio
Coral Gables, Fl 33198

and
7120 W Harbison Avenue
Boca Raton, Florida 33467

Requirements
Must have
• I guess the logo we provide so it is consistent with the new website etc

```html
<!DOCTYPE html>
<html lang="en">
<head>
<meta charset="utf-8">
<title>AskMarlene Business Card</title>
<link href="https://fonts.googleapis.com/css2?family=Carlito:ital,wght@0,400;0,700;1,400&family=Marck+Script&display=swap" rel="stylesheet">
<style>
  :root {
    --paper: #ffffff;
    --ink: #111111;
    --pink: #e0167f;
    --red: #d4202a;
    --cyan: #1fa9e1;
    --band: #0a0a0a;
    --grey-light: #f4f4f4;
    --grey-mid: #c9c9c9;
    --photo-warm: #c9a27e;
    --photo-light: #e8d6c3;
    --photo-bw: #9a9a9a;
  }
  * { margin: 0; padding: 0; box-sizing: border-box; }
  html, body { width: 688px; height: 1200px; overflow: hidden; background: var(--paper); }
  body { position: relative; font-family: "Carlito", "Calibri", sans-serif; color: var(--ink); }

  .crop-marks { position: absolute; inset: 0; width: 688px; height: 1200px; }
  .crop-marks line { stroke: var(--ink); stroke-width: 1.6; }

  /* Front */
  .card-front { position: absolute; left: 98px; top: 72px; width: 499px; height: 285px; }
  .front-portrait {
    position: absolute; left: 0; top: 0; width: 255px; height: 285px;
    background: linear-gradient(160deg, var(--photo-light) 0%, var(--photo-warm) 55%, #a07a58 100%);
  }
  .front-figure {
    position: absolute; left: 0; top: 126px; width: 54px; height: 159px;
    background: linear-gradient(180deg, #f0ebe6 0%, #d9b593 60%, #b78d68 100%);
    box-shadow: 2px 2px 4px rgba(0,0,0,.35);
  }
  .front-panel {
    position: absolute; left: 255px; top: 0; width: 244px; height: 285px;
    background: linear-gradient(180deg, var(--grey-light) 0%, #e2e2e2 45%, var(--grey-mid) 100%);
    border: 1px solid var(--cyan); border-left: none;
    text-align: center;
  }
  .name-script { font-family: "Marck Script", cursive; color: var(--pink); font-weight: 400; }
  .front-panel .name-script { margin-top: 26px; font-size: 33px; line-height: 1; }
  .front-panel .credentials { margin-top: 6px; font-size: 15px; line-height: 23px; }
  .front-rule { position: absolute; left: 0; right: 0; top: 125px; height: 4px; background: var(--red); }
  .front-quote {
    position: absolute; left: 16px; right: 8px; top: 147px;
    font-style: italic; font-size: 11.5px; line-height: 15px; text-align: left;
  }
  .front-quote p + p { margin-top: 6px; text-align: center; }
  .front-quote .signature { margin-top: 10px; text-align: right; }
  .front-band {
    position: absolute; left: 0; right: 0; bottom: 0; height: 51px; background: var(--band);
    display: flex; align-items: center; padding-left: 14px; gap: 12px;
  }
  .brand-name { color: var(--paper); font-weight: 700; font-size: 17px; }
  .band-tagline { color: #cfcfcf; font-size: 5.5px; letter-spacing: 1px; text-transform: uppercase; }

  /* Back */
  .card-back {
    position: absolute; left: 202px; top: 545px; width: 283px; height: 496px;
    border: 2px solid var(--cyan); background: var(--paper);
  }
  .back-photo {
    position: absolute; left: 86px; top: 0; width: 108px; height: 158px;
    background: linear-gradient(180deg, #e4e4e4 0%, var(--photo-bw) 60%, #cfcfcf 100%);
    display: flex; align-items: center; justify-content: center;
  }
  .back-photo .brand-name { color: var(--ink); font-size: 16px; margin-top: 10px; }
  .back-heading { position: absolute; left: 0; right: 0; top: 162px; text-align: center; }
  .back-heading .name-script { font-size: 30px; line-height: 1; }
  .back-heading .credentials { font-size: 14px; line-height: 19px; margin-top: 4px; }
  .back-heading .tagline { font-size: 11px; line-height: 13px; }
  .locations { position: absolute; left: 16px; top: 258px; font-size: 13.5px; line-height: 16px; }
  .locations h2 { font-size: 13.5px; font-weight: 700; }
  .locations address { font-style: normal; }
  .locations address + address { margin-top: 19px; }
  .contact { position: absolute; left: 0; right: 0; top: 398px; text-align: center; font-size: 13.5px; line-height: 18px; }
</style>
</head>
<body>
  <svg class="crop-marks" viewBox="0 0 688 1200" aria-hidden="true">
    <line x1="80" y1="18" x2="80" y2="54"/><line x1="614" y1="18" x2="614" y2="54"/>
    <line x1="45" y1="72" x2="80" y2="72"/><line x1="614" y1="72" x2="650" y2="72"/>
    <line x1="45" y1="356" x2="80" y2="356"/><line x1="614" y1="356" x2="650" y2="356"/>
    <line x1="80" y1="375" x2="80" y2="410"/><line x1="614" y1="375" x2="614" y2="410"/>
    <line x1="202" y1="491" x2="202" y2="526"/><line x1="485" y1="491" x2="485" y2="526"/>
    <line x1="148" y1="544" x2="183" y2="544"/><line x1="504" y1="544" x2="539" y2="544"/>
    <line x1="148" y1="1041" x2="183" y2="1041"/><line x1="504" y1="1041" x2="539" y2="1041"/>
    <line x1="202" y1="1061" x2="202" y2="1095"/><line x1="485" y1="1061" x2="485" y2="1095"/>
  </svg>

  <section class="card-front">
    <div class="front-portrait" role="img" aria-label="Portrait photo of the consultant with long blonde hair"></div>
    <div class="front-figure" role="img" aria-label="Full-length fitness photo of the consultant"></div>
    <div class="front-panel">
      <h1 class="name-script">Marlene Tovak</h1>
      <p class="credentials">Registered Nurse and Certified<br>Sports Nutrionist (R.N., C.S.N.)</p>
      <div class="front-rule"></div>
      <blockquote class="front-quote">
        <p>“Ask me... and I will help you find a way to reach YOUR goals.</p>
        <p>I will “nurse” you into the body you desire.”</p>
        <p class="signature">Marlene Tovak, R.N., C.S.N.</p>
      </blockquote>
      <div class="front-band">
        <span class="brand-name">AskMarlene</span>
        <span class="band-tagline">Personalized Nutrition &amp; Fitness Architecture</span>
      </div>
    </div>
  </section>

  <section class="card-back">
    <div class="back-photo" role="img" aria-label="Black and white photo of the consultant holding red apples">
      <span class="brand-name">AskMarlene</span>
    </div>
    <div class="back-heading">
      <h1 class="name-script">Marlene Tovak</h1>
      <p class="credentials">Registered Nurse and Certified Sports<br>Nutrionist (R.N., C.S.N.)</p>
      <p class="tagline">Personalized Nutrition and Fitness Architecture</p>
    </div>
    <div class="locations">
      <h2>Our Locations:</h2>
      <address>2817 Willowmere Lane<br>Coral Gables, Fl 33198<br>(inside Palmetto Glow Studio)</address>
      <address>7120 W Harbison Avenue<br>Boca Raton, Florida 33467</address>
    </div>
    <div class="contact">
      <p>1-800-555-0147 office</p>
      <p>(305) 555-0182 cell</p>
      <p>website www.askmarlene-example.com</p>
      <p>marlene@askmarlene-example.com</p>
    </div>
  </section>
</body>
</html>
```